We are looking for a 2-page (front and back) 3.67" x 8.5" rack card. . Please refer back to our other Rack Cards for a similar look and feel to the card. This one is titled: Myths and Truths About Memory Loss
The document is for older readers. Do not put text over graphics and keep it simple and easy to read with high contrast.
We want some very simple design element(s) incorporated that convey Native American communities or heritage. But NO headdress, teepee graphics, owls etc. I have included some graphics, please use your creative discretion to use which ones look good on the cards. Please remember to include the funding statement - it can be in a very small font 6/7 point. For more information about our project, please visit https://orvelmesa.net/mind-care/library - This rack card is supported by the Bureau for Wellness Tracking and Outreach (BWT) of the Federal Office of Family and Care Affairs (FOF) as part of a financial assistance award totaling $1,248,600.00 with 100 percent funded by BWT/FOF. The contents are those of the author(s) and do not necessarily represent the official views of, nor an endorsement, by BWT/FOF, or the U.S. Government.
Please feel free to choose one of each of the 2 logos that looks best. We have the QT7 logo and the Mind Wellness Support Hub logo we would like to add. I have added the document and there are images to choose from to use in the rack card. We definitely want to incorporate the coyote in this rack card since it is culturally significant.

```html
<!DOCTYPE html>
<html lang="en">
<head>
<meta charset="utf-8">
<title>Myths and Truths About Memory Loss – Rack Card</title>
<link rel="stylesheet" href="https://fonts.googleapis.com/css2?family=Barlow:wght@400;500;600;700&family=Barlow+Condensed:wght@400;500&family=Montserrat:wght@500;700;800&display=swap">
<style>
  :root{
    --bg:#4a4a4a;
    --paper:#ffffff;
    --teal-1:#52aab3;
    --teal-2:#43929a;
    --teal-3:#245058;
    --teal-deep:#1f4a50;
    --cyan:#5fd0da;
    --red-1:#b65a52;
    --red-2:#8f3c38;
    --maroon:#3a1519;
    --ink:#2a2a2a;
    --line:#9cc3c7;
    --band-a:#bcd9db;
    --band-b:#d8aaa4;
  }
  *{box-sizing:border-box;margin:0;padding:0}
  html,body{width:1084px;height:1200px;overflow:hidden;background:var(--bg)}
  body{font-family:"Barlow",sans-serif;color:var(--ink)}
  .stage{position:relative;width:1084px;height:1200px;overflow:hidden}
  .card{position:absolute;top:99px;width:600px;height:1387px;background:var(--paper);
        transform:scale(.7227);transform-origin:0 0;box-shadow:0 6px 18px rgba(0,0,0,.35);overflow:hidden}
  .card--front{left:89px}
  .card--back{left:562px}
  .abs{position:absolute}
  .photo{position:absolute;border-radius:2px}

  .brand{left:52px;top:56px;display:flex;align-items:center;gap:12px;color:var(--teal-1);font-weight:700}
  .brand__mark{width:40px;height:40px;background:var(--teal-1);border-radius:50%}
  .brand__name{font-size:15px;line-height:1.15;letter-spacing:.3px;text-transform:uppercase}
  .brand__name b{font-size:30px;font-weight:700;display:block;line-height:1}

  .hero{left:0;top:125px;width:333px;height:173px;border-radius:0 14px 14px 0;
        background:linear-gradient(135deg,#2d6169,#173b40);padding:22px 0 0 52px;color:#fff}
  .hero__line1{font-family:"Montserrat",sans-serif;font-weight:800;font-size:40px;line-height:1}
  .hero__line1 span{font-weight:500}
  .hero__line2{font-family:"Montserrat",sans-serif;font-weight:800;font-size:62px;line-height:1;color:var(--cyan);margin-top:2px}
  .hero__line3{display:flex;align-items:center;gap:8px;margin-top:6px;font-family:"Montserrat",sans-serif;font-weight:800;font-size:18px}
  .pill-red{background:var(--red-1);border-radius:16px;padding:3px 12px;font-size:18px}

  .band{position:absolute;left:0;width:600px;height:18px;background:linear-gradient(90deg,var(--band-a),var(--band-b),var(--band-a))}

  .body-text{font-size:18px;line-height:21.8px;color:var(--ink)}

  .myths{position:absolute;left:52px;width:496px;border:1.5px solid var(--line);border-radius:22px}
  .vs{position:absolute;left:192px;width:216px;height:32px;display:flex;align-items:center;
      font-family:"Montserrat",sans-serif;font-weight:800;font-size:20px;color:#fff}
  .vs__myth{background:var(--teal-3);height:32px;flex:1;border-radius:16px 0 0 16px;display:flex;align-items:center;justify-content:center;padding-right:14px}
  .vs__truth{background:var(--maroon);height:32px;flex:1;border-radius:0 16px 16px 0;display:flex;align-items:center;justify-content:center;padding-left:14px}
  .vs__badge{position:absolute;left:90px;top:-3px;width:36px;height:38px;border-radius:50%;background:var(--red-1);
             border:2px solid #fff;font-family:"Barlow",sans-serif;font-weight:500;font-size:14px;display:flex;align-items:center;justify-content:center}
  .cell{position:absolute;width:230px;padding:20px 12px 0 16px;font-size:18px;line-height:21.8px;color:#fff}
  .cell--myth{left:63px}
  .cell--truth{left:305px;font-weight:500}
  .t1{background:var(--teal-1)} .t2{background:var(--teal-2)} .t3{background:var(--teal-3)}
  .r1{background:var(--red-1)} .r2{background:var(--red-2)} .r3{background:var(--maroon)}

  .quote-mark{font-family:"Montserrat",sans-serif;font-weight:800;font-size:56px;color:var(--red-1);line-height:1}
  .quote{left:198px;top:1130px;width:360px;font-weight:700;font-size:17.5px;line-height:21.8px;color:#1e1e1e}
  .quote-name{left:198px;top:1208px;font-weight:700;font-size:20px;color:var(--teal-deep)}
  .quote-src{left:198px;top:1236px;font-size:14.5px;color:var(--red-2);font-weight:500}

  .footer{position:absolute;left:0;width:600px;background:var(--teal-1);color:#fff}
  .footer__url{position:absolute;left:0;width:600px;text-align:center;font-family:"Montserrat",sans-serif;font-weight:700;font-size:22px;letter-spacing:7px}
  .funding{position:absolute;left:52px;top:16px;width:496px;text-align:center;font-size:12.6px;line-height:16.3px}

  .section-tag{left:55px;top:580px;height:31px;width:222px;background:var(--maroon);border-radius:0 16px 16px 0;
               border-left:5px solid var(--teal-3);color:#fff;font-family:"Montserrat",sans-serif;font-weight:800;font-size:18px;
               display:flex;align-items:center;padding-left:14px}
  .res-head{left:52px;top:916px;font-family:"Montserrat",sans-serif;font-weight:800;font-size:17.5px;color:var(--maroon)}
  .res-line{left:54px;font-size:16.5px;color:var(--ink)}
  .res-line b{font-weight:600}
  .url-pill{position:absolute;left:52px;height:28px;border-radius:14px;background:var(--teal-deep);color:#fff;
            font-family:"Barlow Condensed",sans-serif;font-size:14px;display:flex;align-items:center;padding:0 14px}
</style>
</head>
<body>
<div class="stage">

  <section class="card card--front">
    <div class="abs brand">
      <span class="brand__mark"></span>
      <span class="brand__name"><b>QT7</b>Northern Circle Alliance for Elder Wellness</span>
    </div>

    <div class="photo" role="img" aria-label="Photo of an Elder couple outdoors, the man standing beside the seated woman"
         style="left:338px;top:125px;width:208px;height:173px;background:linear-gradient(160deg,#b9704f,#8a5a3d 55%,#c9b9a6)"></div>

    <div class="abs hero">
      <div class="hero__line1">MYTHS <span>AND</span></div>
      <div class="hero__line2">TRUTHS</div>
      <div class="hero__line3">ABOUT <span class="pill-red">MEMORY LOSS</span></div>
    </div>

    <div class="band" style="top:300px" role="img" aria-label="Woven zigzag border pattern"></div>

    <div class="photo" role="img" aria-label="Illustration of a grandmother and a young girl riding in a canoe"
         style="left:22px;top:330px;width:250px;height:238px;background:linear-gradient(150deg,#e9e2ea,#a9b7d0 50%,#5fb3bb)"></div>

    <p class="abs body-text" style="left:286px;top:346px;width:266px">People sometimes believe things about memory loss that are not true. Misunderstandings can make it harder for Elders in Native communities to get the help they need when they start having memory issues. Below are some common myths and truths about memory loss, Alzheimer’s disease, and related dementias.</p>

    <div class="myths" style="top:604px;height:464px"></div>
    <div class="vs" style="top:588px">
      <span class="vs__myth">MYTH</span><span class="vs__truth">TRUTH</span><span class="vs__badge">VS</span>
    </div>

    <div class="cell cell--myth t1" style="top:634px;height:78px">Getting Alzheimer’s is a normal part of aging</div>
    <div class="cell cell--truth r1" style="top:634px;height:78px">It is a disease that not everyone will get</div>
    <div class="cell cell--myth t2" style="top:720px;height:162px">Memory problems and forgetfulness are definite signs of dementia</div>
    <div class="cell cell--truth r2" style="top:720px;height:162px">Memory problems do not solely determine if they are dementia. Other medical conditions can cause memory problems. Talk to your doctor</div>
    <div class="cell cell--myth t3" style="top:891px;height:162px">Only older people can get Alzheimer’s disease</div>
    <div class="cell cell--truth r3" style="top:891px;height:162px">There have been cases for people as young as twenty-five, though it is rare to undergo treatment</div>

    <div class="photo" role="img" aria-label="Photo of a seated Elder woman in a light traditional dress"
         style="left:22px;top:1080px;width:155px;height:190px;background:linear-gradient(170deg,#dfe6f2,#a9bde0 60%,#d9d77e)"></div>
    <div class="abs quote-mark" style="left:196px;top:1086px">“</div>
    <p class="abs quote">Every morning brings a fresh chance to learn, to laugh, and to grow a little kinder than the day before</p>
    <div class="abs quote-name">Marla Greyfeather (Stonebrook Band)</div>
    <div class="abs quote-src">Personal communication with the author</div>
    <div class="abs quote-mark" style="left:486px;top:1230px">”</div>

    <div class="band" style="top:1282px" role="img" aria-label="Woven zigzag border pattern"></div>
    <div class="footer" style="top:1300px;height:87px">
      <div class="footer__url" style="top:26px">www.orvelmesa.net</div>
    </div>
  </section>

  <section class="card card--back">
    <div class="myths" style="top:52px;height:508px"></div>
    <div class="vs" style="top:38px">
      <span class="vs__myth">MYTH</span><span class="vs__truth">TRUTH</span><span class="vs__badge">VS</span>
    </div>

    <div class="cell cell--myth t1" style="top:82px;height:126px">People with Alzheimer’s disease cannot be happy</div>
    <div class="cell cell--truth r1" style="top:82px;height:126px;padding-top:8px">A person with memory loss can experience strong moods and emotions but still enjoy life and relationships.</div>
    <div class="cell cell--myth t2" style="top:217px;height:163px">Dementia can be prevented by a certain supplement or food.</div>
    <div class="cell cell--truth r2" style="top:217px;height:163px">Healthy eating may help overall wellness, including brain health. No additional supplements will completely prevent the onset of dementia.</div>
    <div class="cell cell--myth t3" style="top:387px;height:163px">Alzheimer’s is reversible through prescription drugs</div>
    <div class="cell cell--truth r3" style="top:387px;height:163px">There are prescription drugs to address symptoms of Alzheimer’s and dementia, but there are no medicines that can reverse them.</div>

    <div class="abs section-tag">WHAT YOU CAN DO</div>
    <p class="abs body-text" style="left:54px;top:623px;width:240px">If you or someone you love is having memory problems, do not wait. Talk to a healthy provider you trust. Learning the truth can help keep our Elders strong and supported.</p>

    <div class="photo" role="img" aria-label="Photo of a coyote walking through golden grassland"
         style="left:305px;top:580px;width:241px;height:183px;background:linear-gradient(180deg,#c9a27c,#9d8368 55%,#b99a76)"></div>
    <div class="photo" role="img" aria-label="Photo of a river winding through a forested canyon"
         style="left:54px;top:775px;width:241px;height:120px;background:linear-gradient(180deg,#9fc3e0,#4f7a3c 40%,#3b5f2e)"></div>
    <div class="photo" role="img" aria-label="Photo of a horseshoe river bend in red rock canyon"
         style="left:305px;top:775px;width:241px;height:120px;background:radial-gradient(circle at 55% 55%,#2f8aa0 0 22%,#c4744e 30%,#d99a6f 80%)"></div>

    <div class="abs res-head">12 COMMON ALZHEIMER’S DISEASE MYTHS</div>
    <div class="abs res-line" style="top:943px">12 Common Alzheimer's Disease Myths – <b>ElderHaven.net</b></div>
    <div class="url-pill" style="top:977px;width:328px">https://www.elderhaven.net/c/memory-myths-busted/</div>
    <div class="abs res-line" style="top:1011px">Memory Care Network – Myths vs. Facts</div>
    <div class="url-pill" style="top:1041px;width:496px">https://www.memorycarenet.org/dementia/research-and-progress/myths-vs-facts</div>
    <div class="abs res-line" style="top:1075px">QT7 Brain Health Resources</div>
    <div class="url-pill" style="top:1103px;width:192px">https://orvelmesa.net/resources/</div>

    <div class="band" style="top:1154px" role="img" aria-label="Woven zigzag border pattern"></div>
    <div class="footer" style="top:1172px;height:215px">
      <p class="funding">For more information about our project, please visit https://orvelmesa.net/mind-care/library - This rack card is supported by the Bureau for Wellness Tracking and Outreach (BWT) of the Federal Office of Family and Care Affairs (FOF) as part of a financial assistance award totaling $1,248,600.00 with 100 percent funded by BWT/FOF. The contents are those of the author(s) and do not necessarily represent the official views of, nor an endorsement, by BWT/FOF, or the U.S. Government.</p>
      <div class="footer__url" style="top:154px">www.orvelmesa.net</div>
    </div>
  </section>

</div>
</body>
</html>
```